A new presentation to our clients

we are a Real Estate agency, our website is www.dorelumia.com and it’s time to have a new, fashion and remarcable Business Card. we want to differentiate ourselves from other companies so we want a business card that differentiates us. we want the business card to impact our customers. in the competitive market that we have today, we have to be different and it is this difference that we seek

Target Market(s)

Real Estate Clients

Contact Information for Business Card

We search a totaly diferent card from the usual

Font styles to use
Sans Serif

Colors
e34197

Requirements
Must have
• Logo, adress, phone contact, e-mail, photo, and our website
Nice to have
• We would like to see a modern business card
Should not have
• Houses or building draws

```html
<!DOCTYPE html>
<html lang="en">
<head>
<meta charset="utf-8">
<title>Dore Lumia — Business Card</title>
<link rel="stylesheet" href="https://fonts.googleapis.com/css2?family=Open+Sans:wght@400;600&family=Roboto:wght@700&display=swap">
<style>
  :root {
    --brand-pink: #e5226d;
    --brand-pink-deep: #d81b62;
    --card-white: #fbfbfb;
    --card-mist: #eeeeee;
    --silver: #e8e8ea;
    --text-light: #ffffff;
    --stage: #e9e7e6;
  }
  * { margin: 0; padding: 0; box-sizing: border-box; }
  html, body {
    width: 1200px; height: 900px; overflow: hidden;
    background: var(--stage);
  }
  .stage { position: relative; width: 1200px; height: 900px; }
  .business-card {
    position: absolute; left: 150px; top: 172px;
    width: 652px; height: 403px;
    transform: scale(1.3804); transform-origin: 0 0;
    background: linear-gradient(180deg, var(--card-white) 0%, var(--card-mist) 55%);
    overflow: hidden;
    box-shadow: 0 6px 20px rgba(0,0,0,0.12);
    font-family: "Open Sans", sans-serif;
    color: var(--text-light);
  }
  .card-band { position: absolute; inset: 0; width: 652px; height: 403px; }
  .brand-name {
    position: absolute; left: 0; right: 0; top: 78px;
    text-align: center;
    font-family: "Open Sans", sans-serif; font-weight: 600;
    font-size: 60px; letter-spacing: 1px;
    color: var(--brand-pink);
  }
  .person {
    position: absolute; right: 342px; top: 276px; text-align: right;
  }
  .person-name {
    font-family: "Roboto", sans-serif; font-weight: 700;
    font-size: 22px; line-height: 1.1; letter-spacing: 0.2px;
  }
  .person-role { font-size: 16px; line-height: 1.3; }
  .divider {
    position: absolute; left: 325px; top: 254px;
    width: 1px; height: 86px; background: rgba(255,255,255,0.55);
  }
  .contact-list {
    position: absolute; left: 339px; top: 251px; list-style: none;
  }
  .contact-list li {
    display: flex; align-items: center; gap: 8px;
    font-size: 16.5px; line-height: 23.5px;
  }
  .contact-list svg { width: 15px; height: 15px; fill: var(--text-light); flex: none; }
  .address {
    position: absolute; left: 0; right: 0; top: 354px;
    text-align: center; font-size: 16px; white-space: pre;
  }
</style>
</head>
<body>
<main class="stage">
  <section class="business-card">
    <svg class="card-band" viewBox="0 0 652 403" aria-hidden="true">
      <path d="M0 203 Q326 252 652 201 L652 403 L0 403 Z" fill="var(--brand-pink)"/>
      <path d="M0 196 Q326 246 652 195" fill="none" stroke="var(--silver)" stroke-width="6"/>
      <path d="M0 188 Q326 240 652 187" fill="none" stroke="var(--brand-pink-deep)" stroke-width="4"/>
    </svg>

    <h1 class="brand-name">Dore Lumia</h1>

    <div class="person">
      <p class="person-name">RAFAEL MOREIRA</p>
      <p class="person-role">Managing Director</p>
    </div>

    <span class="divider"></span>

    <ul class="contact-list">
      <li>
        <svg viewBox="0 0 16 16" aria-hidden="true"><path d="M1 5c0-2 3-3 7-3s7 1 7 3v1h-4V4.5H5V6H1z"/><path d="M4 7h8l2 7H2z"/><circle cx="8" cy="10.5" r="1.8" fill="var(--brand-pink)"/></svg>
        (+351) 210 555 140
      </li>
      <li>
        <svg viewBox="0 0 16 16" aria-hidden="true"><path d="M4 1h8v4H4z"/><path d="M1 6h14v6h-3v-2H4v2H1z"/><path d="M4 11h8v4H4z"/></svg>
        (+351) 210 555 149
      </li>
      <li>
        <svg viewBox="0 0 16 16" aria-hidden="true"><path d="M1 3h14v10H1z"/><path d="M1.5 3.5 8 9l6.5-5.5" fill="none" stroke="var(--brand-pink)" stroke-width="1.4"/></svg>
        geral@dorelumia.com
      </li>
      <li>
        <svg viewBox="0 0 16 16" aria-hidden="true"><circle cx="8" cy="8" r="7"/><path d="M5 4c2 1 1 3 3 3s1 3 3 3M9 3c1 1 3 1 3 3" fill="none" stroke="var(--brand-pink)" stroke-width="1.3"/></svg>
        www.dorelumia.com
      </li>
    </ul>

    <p class="address">Rua das Flores Claras, 118  4400-052, Vila Nova de Gaia</p>
  </section>
</main>
</body>
</html>
```